Gutscheine
Zielgruppe
Immobilienmakler, Verkauf und Vermietung, Immobilienbewertung
Aufgabenstellung
Es soll eine Gutscheinkarte werden für die Verteilung auf einen Stadtfest am Stand vor unserem Büro.
Es soll ein Bezug zu Immobilien haben, aber auch eine Emotion vermitteln. Daher Bild mit Familie oder Rentner. Zielgruppe sollen sein zum einen junge Leute, die vor haben eine Immobilie zu kaufen. Und auf der anderen Seite Leute, die mit dem Gedanken spielen eine Immobilie aus Altersgründen, Trennung, Scheidung oder nach Erbe zu verkaufen. Dominant soll mit dem Gutschein zur kostenlosen Bewertung einer Immobilie gelockt werden.
Auf der Rückseite soll es so sein, dass Kunden ankreuzen können, ob Sie eine Immobilie evtl. Verkaufen möchten und eine kostenlose Bewertung wünschen.
Evtl. macht es Sinn zwei Karten anzulegen. Einmal Zielgruppe Käufer/Suchende, einmal Verkäufer.
Beim Format bin ich flexibel und für alles . Es kann länglich sein, aber auch quadratisch.
Vom Design einen Bezug zu den bisherigen Flyern und Broschüren im Anhang.
Bilder die auf der Homepage sind, sind als Stockbilder vorhanden.
Es werden noch einige andere Sachen für das Stadtfest benötigt. Wie Bierdeckel, Imagebroschüre zum Aufklappen, Banner, Roll-Up, Luftballons.

```html
<!DOCTYPE html>
<html lang="de">
<head>
<meta charset="utf-8">
<title>Gutscheinkarten – Maren Immobilien</title>
<link href="https://fonts.googleapis.com/css2?family=Playfair+Display:wght@400&family=Exo+2:wght@400;500;600&display=swap" rel="stylesheet">
<style>
:root{
  --navy:#1c355e;
  --gold:#b9a257;
  --stage:#5a5a5a;
  --white:#ffffff;
  --ink:#1d1d1f;
}
*{margin:0;padding:0;box-sizing:border-box}
html,body{width:1200px;height:574px;overflow:hidden;background:var(--stage)}
.canvas{position:relative;width:1200px;height:574px}
.card{position:absolute;width:564px;height:265px;overflow:hidden;background:var(--white)}
.card--front-seller{left:15px;top:16px}
.card--front-buyer{left:626px;top:16px}
.card--back-seller{left:15px;top:298px}
.card--back-buyer{left:626px;top:298px}

.photo{position:absolute}
.photo--couple{left:0;top:0;width:462px;height:265px;background:linear-gradient(135deg,#f4f3f0 0%,#e6e4df 45%,#d9d6cf 100%)}
.photo--living{left:0;top:0;width:564px;height:265px;background:linear-gradient(180deg,#dcdcda 0%,#a9a8a3 45%,#6d6a63 75%,#8a8580 100%)}

.band-gold{position:absolute;background:var(--gold)}
.panel-navy{position:absolute;background:var(--navy)}
.offer{position:absolute;background:var(--navy);outline:1px solid var(--white);outline-offset:3px;
  display:flex;align-items:center;justify-content:flex-end;padding-right:8px;
  font-family:"Exo 2",sans-serif;font-weight:600;color:var(--white);font-size:14.5px;line-height:17px;text-align:right;letter-spacing:.3px}
.web{position:absolute;display:flex;align-items:center;gap:8px;font-family:Arial,Helvetica,sans-serif;font-size:8.5px;color:var(--white)}
.web svg{width:10px;height:10px}

.voucher-title{position:absolute;font-family:"Playfair Display",serif;font-variant:small-caps;font-size:39px;line-height:1;letter-spacing:.5px}
.voucher-title--navy{color:var(--navy)}
.voucher-title--white{color:var(--white)}

.brand-chip{position:absolute;display:flex;align-items:center;justify-content:center;font-family:"Playfair Display",serif;font-size:9px;letter-spacing:1px}
.brand-chip--gold{left:27px;top:27px;width:41px;height:41px;background:var(--gold);color:var(--white);outline:1px solid var(--gold);outline-offset:2px}
.brand-chip--white{left:30px;top:179px;width:56px;height:56px;background:var(--white);color:var(--navy);outline:1px solid var(--white);outline-offset:3px;font-size:11px}

.check-title{position:absolute;left:26px;font-family:"Playfair Display",serif;font-variant:small-caps;font-size:17px;color:var(--navy);letter-spacing:.3px}
.check-item{position:absolute;left:26px;display:flex;align-items:center;gap:8px;font-family:"Exo 2",sans-serif;font-size:11px;color:var(--ink);letter-spacing:.2px}
.check-item .box{width:11px;height:11px;border:1px solid #555}
.phone-field{position:absolute;left:26px;top:180px;font-family:"Exo 2",sans-serif;font-size:11px;color:var(--ink);letter-spacing:.2px}

.brand{position:absolute;left:446px;top:26px;width:104px;text-align:center}
.brand .mark{width:58px;height:58px;margin:0 auto;background:var(--gold);outline:1px solid var(--gold);outline-offset:2px}
.brand .name{margin-top:10px;font-family:"Playfair Display",serif;font-size:15px;letter-spacing:2px;color:var(--navy)}

.contact{position:absolute;left:443px;font-family:"Exo 2",sans-serif;font-size:7.5px;line-height:9.3px;color:var(--gold);letter-spacing:.3px}
.contact svg{position:absolute;left:0;top:0;width:9px;height:9px}
.contact span{display:block;padding-left:13px}
.contact--phone{top:188px}
.contact--address{top:204px}

.footer-band{position:absolute;left:0;top:239px;width:300px;height:26px;background:var(--gold)}
.footer-band::after{content:"";position:absolute;right:-8px;top:0;width:8px;height:26px;background:var(--navy)}
</style>
</head>
<body>
<main class="canvas">

  <!-- Vorderseite Eigentümer -->
  <section class="card card--front-seller">
    <div class="photo photo--couple" role="img" aria-label="Fröhliches älteres Paar springt Hand in Hand auf einem Bett in einem hellen Schlafzimmer"></div>
    <div class="band-gold" style="left:462px;top:0;width:102px;height:265px"></div>
    <div class="panel-navy" style="left:415px;top:42px;width:149px;height:182px"></div>
    <div class="offer" style="left:346px;top:81px;width:187px;height:104px">Kostenlose<br>Wertermittlung<br>&amp; Verkaufsberatung<br>für Eigentümer</div>
    <div class="web" style="left:426px;top:202px">
      <svg viewBox="0 0 12 12" fill="none" stroke="#fff" stroke-width="1"><circle cx="6" cy="6" r="5"/><ellipse cx="6" cy="6" rx="2.2" ry="5"/><line x1="1" y1="6" x2="11" y2="6"/></svg>
      www.maren-immobilien.de
    </div>
    <div class="brand-chip brand-chip--gold">Maren</div>
    <div class="voucher-title voucher-title--navy" style="left:26px;top:210px">Gutschein</div>
  </section>

  <!-- Vorderseite Kaufinteressenten -->
  <section class="card card--front-buyer">
    <div class="photo photo--living" role="img" aria-label="Modernes, helles Wohnzimmer mit Kamin, Sofa, Couchtisch und Essbereich vor großen Fenstern"></div>
    <div class="band-gold" style="left:493px;top:0;width:71px;height:265px"></div>
    <div class="panel-navy" style="left:340px;top:27px;width:153px;height:230px"></div>
    <div class="offer" style="left:286px;top:89px;width:189px;height:105px">Kostenlose<br>Immobilienbewertung<br>&amp; Beratung für<br>Kaufinteressenten</div>
    <div class="web" style="left:358px;top:209px">
      <svg viewBox="0 0 12 12" fill="none" stroke="#fff" stroke-width="1"><circle cx="6" cy="6" r="5"/><ellipse cx="6" cy="6" rx="2.2" ry="5"/><line x1="1" y1="6" x2="11" y2="6"/></svg>
      www.maren-immobilien.de
    </div>
    <div class="voucher-title voucher-title--white" style="left:25px;top:23px">Gutschein</div>
    <div class="brand-chip brand-chip--white">Maren</div>
  </section>

  <!-- Rückseite Eigentümer -->
  <section class="card card--back-seller">
    <h2 class="check-title" style="top:57px">Bitte ankreuzen:</h2>
    <div class="check-item" style="top:106px"><span class="box"></span>Ich möchte den realen Wert meiner Immobilie erfahren</div>
    <div class="check-item" style="top:144px"><span class="box"></span>Ich erwäge einen Verkauf</div>
    <div class="phone-field">Telefon: ____________________________________________</div>
    <div class="brand"><div class="mark"></div><div class="name">MAREN IMMOBILIEN</div></div>
    <div class="contact contact--phone">
      <svg viewBox="0 0 12 12" fill="none" stroke="#b9a257" stroke-width="1"><path d="M2 1.5h2.5l1 2.5-1.5 1a6 6 0 0 0 3 3l1-1.5 2.5 1V10a1 1 0 0 1-1 1A9 9 0 0 1 1 2.5a1 1 0 0 1 1-1z"/></svg>
      <span>02241 48 30 172</span>
    </div>
    <div class="contact contact--address">
      <svg viewBox="0 0 12 12" fill="none" stroke="#b9a257" stroke-width="1"><path d="M6 11s4-4 4-6.5a4 4 0 0 0-8 0C2 7 6 11 6 11z"/><circle cx="6" cy="4.5" r="1.4"/></svg>
      <span>Maren Immobilien</span><span>Lindenweg 18</span><span>53721 Siegburg</span><span>Deutschland</span>
    </div>
    <div class="footer-band"></div>
  </section>

  <!-- Rückseite Kaufinteressenten -->
  <section class="card card--back-buyer">
    <h2 class="check-title" style="top:18px">Bitte ankreuzen:</h2>
    <div class="check-item" style="top:106px"><span class="box"></span>Ich suche eine Immobilie zum Kauf</div>
    <div class="check-item" style="top:144px"><span class="box"></span>Ich möchte eine kostenlose Immobilienbewertung</div>
    <div class="phone-field">Telefon: ____________________________________________</div>
    <div class="brand"><div class="mark"></div><div class="name">MAREN IMMOBILIEN</div></div>
    <div class="contact contact--phone">
      <svg viewBox="0 0 12 12" fill="none" stroke="#b9a257" stroke-width="1"><path d="M2 1.5h2.5l1 2.5-1.5 1a6 6 0 0 0 3 3l1-1.5 2.5 1V10a1 1 0 0 1-1 1A9 9 0 0 1 1 2.5a1 1 0 0 1 1-1z"/></svg>
      <span>02241 48 30 172</span>
    </div>
    <div class="contact contact--address">
      <svg viewBox="0 0 12 12" fill="none" stroke="#b9a257" stroke-width="1"><path d="M6 11s4-4 4-6.5a4 4 0 0 0-8 0C2 7 6 11 6 11z"/><circle cx="6" cy="4.5" r="1.4"/></svg>
      <span>Maren Immobilien</span><span>Lindenweg 18</span><span>53721 Siegburg</span><span>Deutschland</span>
    </div>
    <div class="footer-band"></div>
  </section>

</main>
</body>
</html>
```